Tallyleaf Web Design

Create Website Design for Tallyleaf. Tallyleaf is online application for collaboration team work system (task list management). More concept design for this project please find attach file ("tallyleaf website concept.pdf") . But my concept is just describe minimal features not bind design

For tallyleaf logo, i had already attach files. But i had not decided what color i chose, so it's okay if you suggest logo color for your suitable website design.
Updates

Dear All Designer,

I like brisk carousel (http://quorvanlabs.example/brisk-carousel/),
may be your concept design can adjust with this concept.
but don't worry about script for brisk carousel, my team will be handle
You just make website design to suitable with brisk carousel

but if you had own website design concept are welcome

thanks

Target Market(s)

Business Company

Industry/Entity Type

Management

```html
<!DOCTYPE html>
<html lang="en">
<head>
<meta charset="utf-8">
<title>Tallyleaf — Online Collaboration Team Work</title>
<link href="https://fonts.googleapis.com/css2?family=Montserrat:wght@400;500;600;700&family=Open+Sans:wght@400;600&display=swap" rel="stylesheet">
<style>
  :root {
    --bar-dark: #353535;
    --page-bg: #eeeeee;
    --white: #ffffff;
    --teal: #0f5a6a;
    --logo-teal: #1c4652;
    --green: #8ab60a;
    --green-dark: #4d8a0f;
    --nav-grey: #9a9a9a;
    --text-dark: #2b2b2b;
    --text-body: #3a3a3a;
    --card-border: #e1e1e1;
    --divider: #dcdcdc;
    --footer-muted: #9a9a9a;
    --bezel: #141414;
    --stand: #d6d6d6;
  }
  * { box-sizing: border-box; margin: 0; padding: 0; }
  html, body { width: 1200px; height: 1087px; overflow: hidden; }
  body {
    position: relative;
    background: var(--page-bg);
    font-family: "Montserrat", Arial, sans-serif;
    color: var(--text-body);
  }

  /* Top bar */
  .top-bar {
    position: absolute; left: 0; top: 0; width: 1200px; height: 64px;
    background: var(--bar-dark);
  }
  .call-us {
    position: absolute; left: 151px; top: 16px;
    display: flex; align-items: center; gap: 8px;
    color: var(--white);
  }
  .call-us .label { font-size: 16px; font-weight: 500; }
  .call-us .number { font-size: 20px; font-weight: 600; margin-left: 4px; letter-spacing: .3px; }
  .login-button {
    position: absolute; left: 970px; top: 15px; width: 97px; height: 35px;
    background: linear-gradient(#ffffff, #dedede);
    border: 1px solid #bdbdbd; border-radius: 5px;
    display: flex; align-items: center; justify-content: center; gap: 6px;
    font-size: 17px; font-weight: 600; color: #222;
  }

  /* Header */
  .site-header {
    position: absolute; left: 0; top: 64px; width: 1200px; height: 111px;
    background: var(--white);
    box-shadow: 0 1px 3px rgba(0,0,0,.12);
  }
  .brand {
    position: absolute; left: 151px; top: 24px;
    display: flex; align-items: center; gap: 14px;
  }
  .brand-mark { width: 44px; height: 44px; border-radius: 50%; background: var(--green); }
  .brand-name { font-size: 56px; font-weight: 500; color: var(--logo-teal); letter-spacing: -1px; line-height: 1; }
  .main-nav {
    position: absolute; right: 132px; top: 45px;
    display: flex; gap: 23px;
    font-size: 16.5px; font-weight: 700; color: var(--nav-grey);
  }
  .main-nav .active { color: var(--green); }

  /* Hero */
  .hero-visual { position: absolute; left: 157px; top: 202px; width: 514px; height: 422px; }
  .hero-visual .bezel {
    position: absolute; left: 0; top: 0; width: 514px; height: 345px;
    background: var(--bezel); border-radius: 8px;
    box-shadow: 0 0 0 2px #c9c9c9;
  }
  .hero-visual .screen {
    position: absolute; left: 21px; top: 22px; width: 470px; height: 298px;
    background: linear-gradient(160deg, #d9ecf5, #9cb8c8 55%, #3f4a57);
  }
  .hero-visual .stand {
    position: absolute; left: 200px; top: 345px; width: 129px; height: 77px;
    background: linear-gradient(90deg, #c4c4c4, #ececec 50%, #c4c4c4);
    clip-path: polygon(6% 0, 94% 0, 100% 100%, 0 100%);
  }
  .hero-title {
    position: absolute; left: 703px; top: 210px;
    font-size: 50.5px; font-weight: 700; line-height: 54.5px; color: var(--teal);
    letter-spacing: .3px;
  }
  .hero-text {
    position: absolute; left: 704px; top: 449px;
    font-size: 14.2px; line-height: 18.6px; color: var(--text-dark); white-space: nowrap;
  }
  .slider-dots { position: absolute; left: 965px; top: 610px; display: flex; gap: 8px; }
  .slider-dots span {
    width: 12px; height: 12px; border-radius: 50%;
    background: linear-gradient(#f6f6f6, #cfcfcf); border: 1px solid #b5b5b5;
  }
  .slider-dots .current { background: radial-gradient(#a6d05a, #6c9a22); }
  .section-divider {
    position: absolute; left: 149px; top: 655px; width: 917px; height: 1px;
    background: var(--divider);
  }

  /* Feature cards */
  .feature-card {
    position: absolute; top: 683px; width: 287px; height: 314px;
    background: var(--white); border: 1px solid var(--card-border);
    text-align: center;
  }
  .feature-card .visual { margin: 19px auto 0; width: 248px; height: 146px; }
  .feature-card h2 { margin-top: 16px; font-size: 18.5px; font-weight: 500; color: var(--text-dark); line-height: 24px; }
  .feature-card p { margin-top: 8px; font-size: 12.2px; line-height: 17px; color: var(--text-body); }
  .read-more {
    display: inline-flex; align-items: center; gap: 5px;
    margin-top: 10px; height: 29px; padding: 0 8px;
    background: linear-gradient(#8cc63f, #4f9a14);
    border: 1px solid var(--green-dark); border-radius: 3px;
    color: var(--white); font-size: 12px; font-weight: 600;
  }
  .visual-desktop { background: linear-gradient(135deg, #e4f3cf, #cfeae2 60%, #e8f5e2); }
  .visual-mobile  { background: linear-gradient(135deg, #dff0c7, #d0ebe5 60%, #e6f3e0); }
  .visual-report  { background: linear-gradient(135deg, #f2f2f2, #c9d6e6 50%, #e9b98a); }

  /* Footer */
  .site-footer {
    position: absolute; left: 0; top: 1028px; width: 1200px; height: 59px;
    background: var(--bar-dark);
  }
  .footer-nav {
    position: absolute; left: 152px; top: 10px;
    font-family: "Open Sans", Arial, sans-serif; font-size: 13px; font-weight: 600; color: var(--white);
  }
  .footer-nav .sep { margin: 0 5px; }
  .copyright {
    position: absolute; left: 152px; top: 33px;
    font-family: "Open Sans", Arial, sans-serif; font-size: 11px; color: var(--footer-muted);
  }
  .social-links { position: absolute; left: 958px; top: 15px; display: flex; gap: 4px; }
  .social-links span { width: 25px; height: 25px; border-radius: 4px; }
  .social-a { background: #e8642a; }
  .social-b { background: #3b5d9c; }
  .social-c { background: #3fa3cf; }
  .social-d { background: #2a74ad; }
</style>
</head>
<body>

<div class="top-bar">
  <div class="call-us">
    <svg width="24" height="24" viewBox="0 0 24 24" aria-hidden="true"><path fill="#fff" d="M6.6 2.5l3 3.4c.5.6.5 1.4 0 2L8 9.6c1.2 2.5 3.4 4.7 6 6l1.7-1.6c.6-.5 1.4-.5 2 0l3.3 3c.6.6.6 1.5 0 2.1l-2 2c-.8.8-2 1-3 .6C9.4 19.4 4.6 14.6 2.3 8.1c-.4-1-.2-2.2.6-3l2-2c.5-.6 1.3-.6 1.7-.6z"/></svg>
    <span class="label">Call us on</span>
    <span class="number">(55) 010 284 7719</span>
  </div>
  <div class="login-button">
    <svg width="16" height="18" viewBox="0 0 16 18" aria-hidden="true"><path d="M4 8V5.5a4 4 0 0 1 8 0V8" fill="none" stroke="#8a8a8a" stroke-width="2"/><rect x="1" y="8" width="14" height="10" rx="2" fill="#e7b320"/></svg>
    Login
  </div>
</div>

<header class="site-header">
  <div class="brand">
    <span class="brand-name">tallyleaf</span>
    <span class="brand-mark"></span>
  </div>
  <nav class="main-nav">
    <span class="active">Home</span>
    <span>About Us</span>
    <span>Services</span>
    <span>Products</span>
    <span>Contact Us</span>
  </nav>
</header>

<div class="hero-visual">
  <div class="bezel">
    <div class="screen" role="img" aria-label="Smiling business team on the monitor screen"></div>
  </div>
  <div class="stand"></div>
</div>
<h1 class="hero-title">Customize<br>Online<br>Collaboration<br>Team Work</h1>
<p class="hero-text">Aenean sollicitudin, lorem quis bibendum auctor,<br>nisi elit consequat ipsum, nec sagittis sem<br>nibh id elit.</p>
<div class="slider-dots"><span></span><span></span><span class="current"></span></div>
<div class="section-divider"></div>

<section class="feature-card" style="left:149px">
  <div class="visual visual-desktop" role="img" aria-label="Laptop running the application"></div>
  <h2>Customize Application</h2>
  <p>Proin gravida nibh vel velit auctor<br>aliquet. Aenean sollicitudin.</p>
  <span class="read-more">Read More <svg width="10" height="8" viewBox="0 0 10 8" aria-hidden="true"><path d="M0 4h8M5 1l3 3-3 3" stroke="#fff" stroke-width="1.6" fill="none"/></svg></span>
</section>

<section class="feature-card" style="left:465px">
  <div class="visual visual-mobile" role="img" aria-label="Smartphone showing synced data"></div>
  <h2>Synchronize All Device</h2>
  <p>Proin gravida nibh vel velit auctor<br>aliquet. Aenean sollicitudin.</p>
  <span class="read-more">Read More <svg width="10" height="8" viewBox="0 0 10 8" aria-hidden="true"><path d="M0 4h8M5 1l3 3-3 3" stroke="#fff" stroke-width="1.6" fill="none"/></svg></span>
</section>

<section class="feature-card" style="left:781px">
  <div class="visual visual-report" role="img" aria-label="Printed sales report with charts"></div>
  <h2>Report</h2>
  <p>Proin gravida nibh vel velit auctor<br>aliquet. Aenean sollicitudin.</p>
  <span class="read-more">Read More <svg width="10" height="8" viewBox="0 0 10 8" aria-hidden="true"><path d="M0 4h8M5 1l3 3-3 3" stroke="#fff" stroke-width="1.6" fill="none"/></svg></span>
</section>

<footer class="site-footer">
  <nav class="footer-nav">
    Home<span class="sep">\</span> About Us<span class="sep">\</span> Services<span class="sep">\</span> Products<span class="sep">\</span> Contact Us
  </nav>
  <p class="copyright">Copyright © 2013 Harbor Lane Contracting. All Rights Reserved.</p>
  <div class="social-links">
    <span class="social-a"></span><span class="social-b"></span><span class="social-c"></span><span class="social-d"></span>
  </div>
</footer>

</body>
</html>
```